Business cards for Harbourline Supply Pty Ltd that import building products into Australia from China
Target Market(s)
Business to Business
Industry/Entity Type
Business
Contact Information for Business Card
Front: Logo and Business Name
Rear:
Vernon Asquill
General Manager
Mobile: 0427 196 354
email: vern@harbourlinesupply.com.au
alternative email: vern@ochrefield.com.au
web: www.harbourlinesupply.com.au
Adelaide, Brisbane and Darwin
Colors
ec1f27
fbee3d

```html
<!DOCTYPE html>
<html lang="en">
<head>
<meta charset="utf-8">
<title>Harbourline Supply Pty Ltd — Business Cards</title>
<link rel="stylesheet" href="https://fonts.googleapis.com/css2?family=Tinos:wght@400&display=swap">
<style>
  :root {
    --backdrop: #d4d4d4;
    --card-white: #ffffff;
    --ink: #111111;
    --accent-blue: #1a9ad6;
    --brand-ink: #0d3f4f;
    --front-black: #000000;
    --front-teal: #06485c;
    --front-blue: #00a9ea;
    --corner-yellow: #e8dc4a;
    --corner-olive: #9a9450;
    --corner-grey: #6d6b5e;
  }
  * { margin: 0; padding: 0; box-sizing: border-box; }
  html, body { width: 900px; height: 1200px; overflow: hidden; }
  body {
    background: var(--backdrop);
    font-family: "Tinos", "Times New Roman", serif;
    position: relative;
  }
  .card {
    position: absolute;
    left: 97px;
    width: 706px;
    height: 413px;
    overflow: hidden;
  }
  .card--front {
    top: 147px;
    background: linear-gradient(118deg,
      var(--front-black) 0%,
      var(--front-black) 22%,
      var(--front-teal) 40%,
      var(--front-blue) 58%,
      var(--front-blue) 64%,
      var(--front-teal) 80%,
      var(--front-black) 96%);
  }
  .card--back {
    top: 645px;
    height: 412px;
    background: var(--card-white);
  }
  .corner-fill { position: absolute; inset: 0; width: 706px; height: 412px; }
  .corner-fill stop.tone-yellow { stop-color: var(--corner-yellow); }
  .corner-fill stop.tone-olive { stop-color: var(--corner-olive); }
  .corner-fill stop.tone-grey { stop-color: var(--corner-grey); }
  .brand {
    position: absolute;
    left: 0; right: 0;
    text-align: center;
    font-weight: 400;
    letter-spacing: 0.04em;
    line-height: 1.1;
  }
  .card--front .brand { top: 168px; color: #ffffff; font-size: 40px; }
  .card--back .brand { top: 98px; color: var(--brand-ink); font-size: 32px; }
  .brand__sub { display: block; font-size: 0.45em; letter-spacing: 0.12em; margin-top: 4px; }
  .contact {
    position: absolute;
    left: 0; right: 0;
    top: 196px;
    text-align: center;
    color: var(--ink);
  }
  .contact__name { font-size: 24px; letter-spacing: 0.03em; line-height: 1.1; }
  .contact__role { font-size: 14px; color: var(--accent-blue); letter-spacing: 0.03em; margin-top: 4px; }
  .contact__cities { font-size: 17px; margin-top: 12px; }
  .contact__lines { font-size: 15px; line-height: 21px; margin-top: 12px; }
</style>
</head>
<body>
  <section class="card card--front" aria-label="Card front">
    <p class="brand">HARBOURLINE<span class="brand__sub">SUPPLY PTY LTD</span></p>
  </section>

  <section class="card card--back" aria-label="Card back">
    <svg class="corner-fill" viewBox="0 0 706 412">
      <defs>
        <linearGradient id="corner-tone-left" x1="0" y1="0" x2="1" y2="1">
          <stop offset="0" class="tone-yellow"/>
          <stop offset="0.6" class="tone-olive"/>
          <stop offset="1" class="tone-grey"/>
        </linearGradient>
        <linearGradient id="corner-tone-right" x1="0" y1="1" x2="1" y2="0">
          <stop offset="0" class="tone-grey"/>
          <stop offset="0.4" class="tone-yellow"/>
          <stop offset="1" class="tone-olive"/>
        </linearGradient>
      </defs>
      <path role="img" aria-label="Decorative metallic corner area, top left" fill="url(#corner-tone-left)" d="M0,0 L268,0 Q70,110 0,372 Z"/>
      <path role="img" aria-label="Decorative metallic corner area, bottom right" fill="url(#corner-tone-right)" d="M706,30 Q640,300 440,412 L706,412 Z"/>
    </svg>
    <p class="brand">HARBOURLINE<span class="brand__sub">SUPPLY PTY LTD</span></p>
    <div class="contact">
      <p class="contact__name">VERNON ASQUILL</p>
      <p class="contact__role">GENERAL MANAGER</p>
      <p class="contact__cities">Adelaide, Brisbane and Darwin</p>
      <p class="contact__lines">
        P: 0427 196 354<br>
        E: vern@harbourlinesupply.com.au<br>
        E: vern@ochrefield.com.au<br>
        W: www.harbourlinesupply.com.au
      </p>
    </div>
  </section>
</body>
</html>
```